Simple Business Cards for Self-employed Coach

Simple business card with a design that includes the QLT logo.
Using either only the logo color or additional colors that match the logo.

Meridian Guides reach deeply into the past, gathering wisdom from East and West, while still staying current with the frontiers of new discovery in cognitive science, genetics, and other disciplines. see https://www.brightharborpath.example/what-is-integral-coaching/

Target Market(s)

Coaching Clients in Tokyo /Asia; in business organizations, but also outside

Industry/Entity Type

Life Coaching

Contact Information for Business Card

Lukas Brenning
Certified Meridian Guide

3-2-48 Kamiyoshi
Nakarino 164-0392
Tokyo, Japan

Phone: +81 70 4817 5062
E-Mail: lukas.brenning@mailora.example

Font styles to use
Sans Serif

Colors
00a990

Requirements
Must have
• include uploaded logo
• color fitting with QLT logo color
Nice to have
• simple, elegant design
Should not have
• clutter

```html
<!DOCTYPE html>
<html lang="en">
<head>
<meta charset="utf-8">
<title>QLT – Business Card</title>
<link href="https://fonts.googleapis.com/css2?family=Roboto:wght@400;500;700&display=swap" rel="stylesheet">
<style>
  :root {
    --brand: #0a7a6e;
    --card: #ffffff;
    --backdrop: #e6e7ea;
  }
  * { box-sizing: border-box; margin: 0; padding: 0; }
  html, body {
    width: 1200px;
    height: 800px;
    overflow: hidden;
    background: var(--backdrop);
    font-family: "Roboto", Arial, sans-serif;
  }
  .stage {
    width: 1200px;
    height: 800px;
    display: flex;
    align-items: center;
    justify-content: center;
  }
  .business-card {
    position: relative;
    width: 840px;
    height: 480px;
    background: var(--card);
    color: var(--brand);
  }
  .brand-mark {
    position: absolute;
    left: 78px;
    top: 62px;
    display: flex;
    align-items: center;
    gap: 18px;
  }
  .brand-square {
    width: 58px;
    height: 58px;
    background: var(--brand);
  }
  .brand-name {
    font-weight: 500;
    font-size: 52px;
    letter-spacing: 14px;
    line-height: 1;
    color: var(--brand);
  }
  .divider {
    position: absolute;
    left: 78px;
    right: 78px;
    top: 262px;
    height: 2px;
    background: var(--brand);
  }
  .holder-name {
    position: absolute;
    right: 78px;
    top: 222px;
    font-size: 30px;
    font-weight: 700;
    text-align: right;
  }
  .contact-block {
    position: absolute;
    right: 78px;
    top: 276px;
    text-align: right;
    font-size: 19px;
    line-height: 1.42;
  }
  .holder-title { margin-bottom: 4px; }
  .contact-line {
    display: flex;
    justify-content: flex-end;
    align-items: center;
    gap: 8px;
  }
  .contact-icon {
    width: 18px;
    height: 18px;
    flex: none;
  }
</style>
</head>
<body>
<main class="stage">
  <article class="business-card">
    <div class="brand-mark">
      <span class="brand-square"></span>
      <span class="brand-name">QLT</span>
    </div>

    <h1 class="holder-name">Lukas Brenning</h1>
    <div class="divider"></div>

    <div class="contact-block">
      <p class="holder-title">Certified Meridian Guide</p>
      <p>3-2-48 Kamiyoshi, Nakarino 164-0392</p>
      <p>Tokyo, Japan</p>
      <p class="contact-line">+81 70 4817 5062
        <svg class="contact-icon" viewBox="0 0 18 18" aria-hidden="true">
          <rect width="18" height="18" rx="2" fill="#0a7a6e"/>
          <path d="M5.2 3.8 L7.2 3.6 L8 6.2 L6.8 7.2 Q7.8 9.6 10.4 11 L11.5 9.8 L14.2 10.6 L14 12.6 Q13.4 14.2 11.6 14 Q5 12.6 3.9 6 Q3.8 4.4 5.2 3.8 Z" fill="#ffffff"/>
        </svg>
      </p>
      <p class="contact-line">lukas.brenning@mailora.example
        <svg class="contact-icon" viewBox="0 0 18 18" aria-hidden="true">
          <rect width="18" height="18" rx="2" fill="#0a7a6e"/>
          <rect x="3.5" y="5" width="11" height="8" fill="none" stroke="#ffffff" stroke-width="1.4"/>
          <path d="M3.5 5 L9 9.5 L14.5 5" fill="none" stroke="#ffffff" stroke-width="1.4"/>
        </svg>
      </p>
    </div>
  </article>
</main>
</body>
</html>
```